Kitchen Facelifts Flyer

I would like a flyer to be designed for my domestic kitchen renovation business.
Majority of my projects is to do with kitchen facelifts. This involves only replacing the doors, drawer fronts, panels, benchtop and splashbacks. We leave the carcass as is and therefore able to save the customer money. Visit my website (www.brightpanels.com.au) to learn more.
I have attached the company logo.
I have attached a number of before and after photos which you can use.
I have also attached a text file which has texts which you may use in the flyer.
The size of the flyer will be 100mm x 2100mm
It will be printed double sided.
Feel free to either design for portrait or landscape.
Please note that you don't have to use all the photos, choose the one(s) you think is best.

```html
<!DOCTYPE html>
<html lang="en">
<head>
<meta charset="utf-8">
<title>Bright Panels – Kitchen Facelifts Flyer</title>
<link href="https://fonts.googleapis.com/css2?family=Oswald:wght@400;600&family=Roboto+Condensed:wght@300;400;700&display=swap" rel="stylesheet">
<style>
  :root{
    --brand-red:#c8384a;
    --ink:#3a3a3c;
    --muted:#77777a;
    --paper:#ffffff;
    --panel-grey:#e4e4e6;
    --stage:#e8eaed;
    --photo-warm:#b98a68;
    --photo-light:#dcd6cf;
    --photo-dark:#4a3a33;
  }
  *{box-sizing:border-box;margin:0;padding:0}
  html,body{width:1200px;height:961px;overflow:hidden}
  body{background:var(--stage);font-family:"Roboto Condensed",sans-serif;color:var(--ink);position:relative}

  .flyer{position:absolute;top:36px;width:420px;height:889px;background:var(--paper);overflow:hidden;box-shadow:0 2px 8px rgba(0,0,0,.12)}
  .flyer--back{left:150px}
  .flyer--front{left:630px}

  .photo{position:absolute;background:linear-gradient(135deg,var(--photo-light),var(--photo-warm));}
  .photo--dark{background:linear-gradient(135deg,var(--photo-dark),var(--photo-warm))}
  .photo--white{background:linear-gradient(135deg,#f2efeb,#cfc8c0)}

  /* shared brand name */
  .brand{display:flex;align-items:center;justify-content:center;gap:12px}
  .brand-mark{display:block;background:var(--brand-red);flex:none}
  .brand-name{font-family:"Oswald",sans-serif;font-weight:600;color:var(--brand-red);letter-spacing:2px;text-transform:uppercase;white-space:nowrap}

  /* back side */
  .back-band-top{position:absolute;left:0;top:0;width:100%;height:22px;background:var(--brand-red)}
  .back-collage{position:absolute;left:0;top:22px;width:100%;height:520px;background:#fff}
  .before-label{position:absolute;left:10px;bottom:8px;font-size:14px;color:#fff;font-style:italic}
  .back-brand{position:absolute;left:0;right:0;top:630px}
  .back-brand .brand-mark{width:26px;height:26px}
  .back-brand .brand-name{font-size:42px}
  .back-contact{position:absolute;left:0;right:0;top:770px;text-align:center;font-size:17px;color:var(--ink);font-family:Georgia,serif}
  .back-band-bottom{position:absolute;left:0;bottom:0;width:100%;height:24px;background:var(--brand-red)}

  /* front side */
  .front-collage{position:absolute;left:0;top:0;width:100%;height:430px;background:#f1f1f2}
  .front-copy{position:absolute;left:34px;right:30px;top:450px}
  .headline{font-family:"Oswald",sans-serif;font-weight:600;font-size:40px;line-height:1.08;color:var(--brand-red)}
  .subhead{font-family:"Oswald",sans-serif;font-weight:400;font-size:21px;line-height:1.2;color:var(--ink);margin-top:8px}
  .body-text{font-size:15px;line-height:1.35;color:var(--muted);margin-top:10px}
  .body-text strong{color:var(--brand-red);font-weight:700}
  .disclaimer{font-size:9.5px;line-height:1.3;color:var(--muted);font-style:italic;margin-top:6px}

  .front-brand{position:absolute;left:30px;top:802px;justify-content:flex-start;gap:8px}
  .front-brand .brand-mark{width:14px;height:14px}
  .front-brand .brand-name{font-size:19px;letter-spacing:1px}

  .contact-box{position:absolute;left:196px;top:770px;width:224px;height:92px;background:var(--panel-grey);padding:12px 8px 0 20px}
  .contact-box::before{content:"";position:absolute;left:6px;top:10px;width:5px;height:72px;background:var(--brand-red)}
  .contact-line{font-size:13.5px;line-height:1.3;color:var(--ink);white-space:nowrap}
  .contact-phone{font-family:"Oswald",sans-serif;font-weight:600;font-size:21px;color:var(--brand-red);line-height:1.2}
</style>
</head>
<body>

<section class="flyer flyer--back" aria-label="Flyer back side">
  <div class="back-band-top"></div>
  <div class="back-collage">
    <div class="photo photo--dark" style="left:150px;top:0;width:270px;height:200px" role="img" aria-label="Photo of a finished kitchen with dark timber cabinets"></div>
    <div class="photo" style="left:0;top:40px;width:144px;height:160px" role="img" aria-label="Before photo of an old kitchen"><span class="before-label">Before</span></div>
    <div class="photo photo--white" style="left:0;top:206px;width:210px;height:150px" role="img" aria-label="After photo of a white kitchen facelift"></div>
    <div class="photo" style="left:216px;top:206px;width:204px;height:150px" role="img" aria-label="Photo of a kitchen with timber benchtop"></div>
    <div class="photo photo--white" style="left:0;top:362px;width:420px;height:158px" role="img" aria-label="Photo of a renovated kitchen interior"></div>
  </div>
  <div class="brand back-brand">
    <span class="brand-mark"></span>
    <span class="brand-name">Bright Panels</span>
  </div>
  <div class="back-contact">www.brightpanels.com.au | 1800 274 448</div>
  <div class="back-band-bottom"></div>
</section>

<section class="flyer flyer--front" aria-label="Flyer front side">
  <div class="front-collage">
    <div class="photo photo--white" style="left:0;top:0;width:420px;height:120px" role="img" aria-label="Photo of a bright kitchen ceiling and cabinets"></div>
    <div class="photo photo--white" style="left:8px;top:128px;width:196px;height:92px" role="img" aria-label="Photo of a white kitchen with wall oven"></div>
    <div class="photo photo--white" style="left:212px;top:128px;width:200px;height:92px" role="img" aria-label="Photo of a kitchen with microwave cabinet"></div>
    <div class="photo" style="left:8px;top:228px;width:130px;height:96px" role="img" aria-label="Photo of a kitchen with timber benchtop"></div>
    <div class="photo" style="left:146px;top:228px;width:130px;height:96px" role="img" aria-label="Photo of a kitchen island with timber top"></div>
    <div class="photo photo--white" style="left:284px;top:228px;width:128px;height:96px" role="img" aria-label="Photo of a kitchen sink by the window"></div>
    <div class="photo photo--dark" style="left:8px;top:332px;width:196px;height:92px" role="img" aria-label="Photo of a cooktop and rangehood"></div>
    <div class="photo photo--white" style="left:212px;top:332px;width:200px;height:92px" role="img" aria-label="Photo of white kitchen cabinets"></div>
  </div>

  <div class="front-copy">
    <h1 class="headline">Is your kitchen<br>looking a little dull?</h1>
    <p class="subhead">Get your dream kitchen in 3 days*<br>while savings thousands.</p>
    <p class="body-text">Transform your kitchen with <strong>new doors</strong>, <strong>drawer fronts</strong>, <strong>handles</strong>, <strong>benchtop</strong>, and <strong>splash back</strong>.<br>We do <strong>new cabinets</strong> as well.<br>100% Australian Made with <strong>10 year guarantee</strong></p>
    <p class="disclaimer">*Disclaimer: Project timeframe is dependent on the scope of the project.<br>3 days is our average timeframe for kitchen facelift.</p>
  </div>

  <div class="brand front-brand">
    <span class="brand-mark"></span>
    <span class="brand-name">Bright Panels</span>
  </div>

  <div class="contact-box">
    <p class="contact-line">Call 1800 BRIGHT PANELS</p>
    <p class="contact-phone">(1800 274 448)</p>
    <p class="contact-line">or visit us at BRIGHTPANELS.COM.AU</p>
  </div>
</section>

</body>
</html>
```